Veracor Systems
Business Cards
Veracor Systems - Information Technology
Creative Brief
Professional
Martin Osgood
Vice President
Veracor IT Systems Harbourline Tower 482 Dunmore Ave East,Suite 3100 Toronto ON, M4R 2T7
martin.osgood@veracorsystems-example.ca
www.veracorsystems-example.ca

```html
<!DOCTYPE html>
<html lang="en">
<head>
<meta charset="utf-8">
<title>Veracor Systems – Business Card</title>
<link href="https://fonts.googleapis.com/css2?family=Arimo:wght@400;700&display=swap" rel="stylesheet">
<style>
  :root {
    --page-bg: #e9e6e2;
    --card-bg: #ffffff;
    --brand-blue: #1a8fc8;
    --brand-blue-light: #5cc0ea;
    --brand-blue-dark: #0f6fa3;
    --arc-grey: #6d6f73;
    --text-dark: #3a3b3d;
    --text-muted: #7a7c80;
  }
  * { box-sizing: border-box; margin: 0; padding: 0; }
  html, body {
    width: 1200px; height: 780px; overflow: hidden;
    background: var(--page-bg);
    font-family: "Arimo", Arial, sans-serif;
  }
  .canvas {
    width: 1200px; height: 780px;
    display: flex; align-items: center; justify-content: center;
  }
  .business-card {
    position: relative;
    width: 1050px; height: 600px;
    background: var(--card-bg);
    border-radius: 30px;
    overflow: hidden;
    box-shadow: 0 10px 30px rgba(0,0,0,0.18);
  }
  .card-swoosh {
    position: absolute; inset: 0;
    width: 100%; height: 100%;
  }
  .brand {
    position: absolute; left: 70px; top: 86px;
  }
  .brand-lockup {
    display: flex; align-items: center; gap: 18px;
  }
  .brand-dot {
    width: 62px; height: 62px; border-radius: 50%;
    background: var(--brand-blue);
  }
  .brand-name {
    font-size: 50px; font-weight: 700;
    color: var(--brand-blue);
    letter-spacing: 1px;
    line-height: 1;
  }
  .brand-tagline {
    margin-top: 12px; margin-left: 80px;
    font-size: 11px; font-weight: 700;
    color: var(--text-muted);
    text-transform: uppercase; letter-spacing: 0.5px;
  }
  .person {
    position: absolute; left: 640px; top: 252px;
  }
  .person-name {
    font-size: 28px; font-weight: 700;
    color: var(--brand-blue);
  }
  .person-title {
    margin-top: 6px;
    font-size: 21px; color: var(--text-muted);
  }
  .address {
    position: absolute; left: 70px; top: 360px;
    font-size: 20px; line-height: 1.3;
    color: var(--text-dark);
  }
  .contact-list {
    position: absolute; left: 70px; top: 468px;
    list-style: none;
    font-size: 18px; color: var(--text-dark);
  }
  .contact-list li {
    display: flex; align-items: center; gap: 12px;
    height: 30px;
  }
  .contact-icon { width: 18px; height: 18px; flex: none; }
</style>
</head>
<body>
<main class="canvas">
  <article class="business-card">
    <svg class="card-swoosh" viewBox="0 0 1050 600" preserveAspectRatio="none" aria-hidden="true">
      <defs>
        <linearGradient id="blueBand" x1="0" y1="0" x2="1" y2="1">
          <stop offset="0" stop-color="var(--brand-blue-light)"/>
          <stop offset="0.55" stop-color="var(--brand-blue)"/>
          <stop offset="1" stop-color="var(--brand-blue-dark)"/>
        </linearGradient>
      </defs>
      <path d="M700,0 H1050 V600 H985 C1010,380 930,150 700,0 Z" fill="url(#blueBand)"/>
      <path d="M860,600 C915,430 880,250 770,120 C905,230 965,410 950,600 Z" fill="var(--arc-grey)"/>
      <path d="M950,600 C965,410 905,230 770,120 C930,220 1000,400 985,600 Z" fill="#ffffff"/>
    </svg>

    <header class="brand">
      <div class="brand-lockup">
        <span class="brand-dot"></span>
        <span class="brand-name">VERACOR IT SYSTEMS</span>
      </div>
      <p class="brand-tagline">Managed IT service and support for small and mid-size business</p>
    </header>

    <section class="person">
      <h1 class="person-name">Martin Osgood</h1>
      <p class="person-title">Vice President</p>
    </section>

    <address class="address" style="font-style:normal">
      Harbourline Tower<br>
      482 Dunmore Ave East,Suite 3100<br>
      Toronto ON, M4R 2T7
    </address>

    <ul class="contact-list">
      <li>
        <svg class="contact-icon" viewBox="0 0 20 20" aria-hidden="true"><path d="M5 2 L8 2 L9 6 L7 8 C8 11 9 12 12 13 L14 11 L18 12 L18 15 C18 17 16 18 14 18 C7 17 3 13 2 6 C2 4 3 2 5 2 Z" fill="var(--brand-blue)"/></svg>
        1 (416) 555-0148
      </li>
      <li>
        <svg class="contact-icon" viewBox="0 0 20 20" aria-hidden="true"><rect x="1" y="4" width="18" height="12" rx="2" fill="var(--brand-blue)"/><path d="M2 5 L10 11 L18 5" fill="none" stroke="#fff" stroke-width="1.6"/></svg>
        martin.osgood@veracorsystems-example.ca
      </li>
      <li>
        <svg class="contact-icon" viewBox="0 0 20 20" aria-hidden="true"><circle cx="10" cy="10" r="8.5" fill="none" stroke="var(--brand-blue)" stroke-width="1.6"/><ellipse cx="10" cy="10" rx="3.5" ry="8.5" fill="none" stroke="var(--brand-blue)" stroke-width="1.4"/><path d="M2 10 H18" stroke="var(--brand-blue)" stroke-width="1.4"/></svg>
        www.veracorsystems-example.ca
      </li>
    </ul>
  </article>
</main>
</body>
</html>
```